Redesign projects page on UK roofing website

Hi guys,

We would like to redesign the projects page of our roofing company website; https://www.brindleroofing.com/projects

We would like to keep the top of the page the same (up to the big image). Also the footer design should remain the same.

We would like to have some nice photos of work we have done with a little bit of writing about each project.

This site has a nice projects page layout; https://www.wtpbld.com/projects

Something along those lines would work well for our needs.

Thanks

```html
<!DOCTYPE html>
<html lang="en">
<head>
<meta charset="utf-8">
<title>Brindle Roofing – Projects</title>
<link href="https://fonts.googleapis.com/css2?family=Outfit:wght@300;400;600;700;800&display=swap" rel="stylesheet">
<style>
:root{
  --blue:#0fb0e0;
  --navy:#0b4776;
  --ink:#222;
  --muted:#555;
  --white:#fff;
  --line:#8a8a8a;
}
*{box-sizing:border-box;margin:0;padding:0}
html,body{width:1200px;height:2737px;overflow:hidden}
body{font-family:"Outfit",sans-serif;background:var(--white);color:var(--ink);position:relative}
.abs{position:absolute}

/* hero */
.hero{position:absolute;left:0;top:0;width:1200px;height:600px;
  background:linear-gradient(180deg,#4a4a4a 0%,#6b6b6b 30%,#3a3a3a 60%,#242424 100%)}
.hero-shade{position:absolute;inset:0;background:linear-gradient(90deg,rgba(0,0,0,.15),rgba(0,0,0,.35))}
.brand{position:absolute;left:108px;top:22px;display:flex;align-items:center;gap:10px;color:var(--white);font-size:28px;font-weight:700;letter-spacing:-.5px}
.brand-dot{width:32px;height:32px;border-radius:50%;background:var(--blue)}
.main-nav{position:absolute;top:31px;left:523px;display:flex;gap:27px}
.main-nav a{color:var(--white);font-size:14px;font-weight:700;text-decoration:none}
.quote-btn{position:absolute;left:942px;top:21px;width:154px;height:37px;background:var(--blue);color:var(--white);font-size:14px;font-weight:700;display:flex;align-items:center;justify-content:center}
.hero-title{position:absolute;left:108px;top:255px;font-size:49px;font-weight:800;line-height:60px;color:var(--white)}
.hero-title span{color:var(--blue)}
.hero-aside{position:absolute;left:844px;top:188px;height:267px;border-left:2px solid var(--blue);padding-left:12px;width:250px}
.hero-aside h2{font-size:30px;font-weight:800;line-height:37px;color:var(--white);margin-top:24px}
.hero-aside p{font-size:23px;font-weight:300;line-height:26px;color:var(--white);margin-top:21px}

/* projects */
.section-title{position:absolute;left:0;width:1200px;text-align:center;font-size:30px;font-weight:800;color:var(--navy)}
.tabs{position:absolute;top:745px;left:272px;display:flex;gap:13px}
.tab{width:154px;height:37px;border:2px solid var(--blue);color:var(--blue);font-size:13px;font-weight:700;display:flex;align-items:center;justify-content:center}
.tab.active{background:var(--blue);color:var(--white)}
.card{position:absolute;width:484px;height:353px;background:var(--white);box-shadow:0 2px 8px rgba(0,0,0,.09)}
.card-photo{height:207px}
.card-body{padding:12px 19px}
.card h3{font-size:22px;font-weight:700;color:var(--blue)}
.facts{margin-top:10px;font-size:14px;line-height:19px;display:grid;grid-template-columns:85px 1fr}
.facts dt{font-weight:700;color:var(--navy)}
.facts dd{font-weight:300}
.read-more{margin-top:8px;display:flex;align-items:center;gap:6px;font-size:14px;font-weight:700;color:var(--blue)}
.outline-btn{position:absolute;left:522px;top:1630px;width:154px;height:37px;border:2px solid var(--blue);color:var(--blue);font-size:14px;font-weight:700;display:flex;align-items:center;justify-content:center}

/* form */
.field{position:absolute;border:1px solid var(--line);font-size:14px;font-weight:300;color:var(--muted);padding-left:31px;display:flex;align-items:center}
.field.message{align-items:flex-start;padding-top:33px}
.send-btn{position:absolute;left:689px;top:2214px;width:320px;height:37px;background:var(--blue);color:var(--white);font-size:14px;font-weight:700;display:flex;align-items:center;justify-content:center}

/* footer */
.footer{position:absolute;left:0;top:2350px;width:1200px;height:387px;background:var(--blue);color:var(--white)}
.footer-col{position:absolute;top:75px}
.footer-col h4{font-size:22px;font-weight:800}
.footer-col ul{list-style:none;margin-top:24px}
.footer-col li{font-size:12px;font-weight:300;line-height:27px}
.social li{display:flex;align-items:center;gap:12px;margin-left:-27px}
.social-box{width:14px;height:14px;border:1.5px solid var(--white);border-radius:3px}
.footer-brand{position:absolute;left:857px;top:70px;width:240px}
.footer-brand .name{font-size:30px;font-weight:700;letter-spacing:-.5px}
.footer-brand p{font-size:12px;font-weight:300;line-height:13px;margin-top:7px}
.badges{position:absolute;left:857px;top:237px;display:flex;gap:26px;align-items:center}
.badge{background:rgba(255,255,255,.85)}
.footer-rule{position:absolute;left:0;top:326px;width:1200px;height:1px;background:rgba(255,255,255,.6)}
.copyright{position:absolute;left:108px;top:352px;font-size:11px;font-weight:700}
</style>
</head>
<body>

<header class="hero">
  <div class="hero-shade" role="img" aria-label="Black and white photo of a wet flat commercial roof with ventilation ducts under a cloudy sky"></div>
  <div class="brand"><span class="brand-dot"></span>brindleroofing</div>
  <nav class="main-nav"><a>Service</a><a>Client</a><a>Project</a><a>Team</a><a>Contact</a></nav>
  <div class="quote-btn">Get a quote</div>
  <h1 class="hero-title">Some of our <span>latest</span><br><span>projects.</span></h1>
  <div class="hero-aside">
    <h2>What we're working on</h2>
    <p>Keep an eye on some of the latest installs, refurbs and repairs we've carried out.</p>
  </div>
</header>

<h2 class="section-title" style="top:688px">Our Recent Projects</h2>
<div class="tabs">
  <div class="tab active">Roofing</div>
  <div class="tab">Single Ply</div>
  <div class="tab">Liquid Roofing</div>
  <div class="tab">Steel Roofing</div>
</div>

<article class="card" style="left:107px;top:858px">
  <div class="card-photo" role="img" aria-label="Terrace roof with glass balustrade and colourful picnic benches" style="background:linear-gradient(135deg,#8e949a,#5f6468)"></div>
  <div class="card-body">
    <h3>Kestrel Hospital, Beckton</h3>
    <dl class="facts"><dt>Type</dt><dd>Liquid Waterproofing</dd><dt>Roof size</dt><dd>70m2</dd><dt>Descriptions</dt><dd>March, 2020</dd></dl>
    <div class="read-more">Read More <svg width="12" height="10" viewBox="0 0 12 10"><path d="M0 5h10M6 1l4 4-4 4" stroke="currentColor" stroke-width="1.6" fill="none"/></svg></div>
  </div>
</article>

<article class="card" style="left:609px;top:858px">
  <div class="card-photo" role="img" aria-label="Aerial view of long industrial pitched roofs with skylights" style="background:linear-gradient(135deg,#6d7880,#9aa3aa 50%,#4c555c)"></div>
  <div class="card-body">
    <h3>Marsh Road, Barking</h3>
    <dl class="facts"><dt>Type</dt><dd>Single Skin Overclad</dd><dt>Roof size</dt><dd>2200m2</dd><dt>Descriptions</dt><dd>October, 2020</dd></dl>
    <div class="read-more">Read More <svg width="12" height="10" viewBox="0 0 12 10"><path d="M0 5h10M6 1l4 4-4 4" stroke="currentColor" stroke-width="1.6" fill="none"/></svg></div>
  </div>
</article>

<article class="card" style="left:107px;top:1238px">
  <div class="card-photo" role="img" aria-label="Aerial view of a grey metal roof beside trees and flats" style="background:linear-gradient(135deg,#4d6a3e,#93a2a8 50%,#6f5a48)"></div>
  <div class="card-body">
    <h3>Harlow Lodge, Willesden</h3>
    <dl class="facts"><dt>Type</dt><dd>Single Skin Overclad</dd><dt>Roof size</dt><dd>400m2</dd><dt>Descriptions</dt><dd>August, 2020</dd></dl>
    <div class="read-more">Read More <svg width="12" height="10" viewBox="0 0 12 10"><path d="M0 5h10M6 1l4 4-4 4" stroke="currentColor" stroke-width="1.6" fill="none"/></svg></div>
  </div>
</article>

<article class="card" style="left:609px;top:1238px">
  <div class="card-photo" role="img" aria-label="Flat grey single-ply roof next to a white warehouse wall" style="background:linear-gradient(180deg,#d8d8d8 0%,#c9c9c9 35%,#6b6e70 55%,#55585a)"></div>
  <div class="card-body">
    <h3>Vantor Aerospace, Romford</h3>
    <dl class="facts"><dt>Type</dt><dd>Single-Ply</dd><dt>Roof size</dt><dd>500m2</dd><dt>Descriptions</dt><dd>November, 2020</dd></dl>
    <div class="read-more">Read More <svg width="12" height="10" viewBox="0 0 12 10"><path d="M0 5h10M6 1l4 4-4 4" stroke="currentColor" stroke-width="1.6" fill="none"/></svg></div>
  </div>
</article>

<div class="outline-btn">View More</div>

<h2 class="section-title" style="top:1762px">Get in touch with us?</h2>
<div class="field" style="left:190px;top:1845px;width:404px;height:61px">Name</div>
<div class="field" style="left:606px;top:1845px;width:404px;height:61px">Company</div>
<div class="field" style="left:190px;top:1929px;width:404px;height:61px">E-mail</div>
<div class="field" style="left:606px;top:1929px;width:404px;height:61px">Phone</div>
<div class="field message" style="left:190px;top:2013px;width:820px;height:182px">Enter Your Message</div>
<div class="send-btn">Send Messages</div>

<footer class="footer">
  <div class="footer-col" style="left:108px"><h4>Overview</h4>
    <ul><li>Services</li><li>Clients</li><li>Projects</li><li>Team</li><li>Contact</li></ul></div>
  <div class="footer-col" style="left:358px"><h4>Services</h4>
    <ul><li>Asbestos roof removal</li><li>Steel cladding</li><li>Liquid waterproofing</li><li>Mastic asphalt roofing</li><li>Single ply roofing</li><li>Roof repairs</li><li>Emergency roof repairs</li></ul></div>
  <div class="footer-col" style="left:606px"><h4>Legal</h4>
    <ul><li>Terms of service</li></ul>
    <h4 style="margin-top:20px">Follow us</h4>
    <ul class="social" style="margin-top:18px"><li><span class="social-box"></span>LinkedIn</li><li><span class="social-box"></span>Instagram</li></ul></div>
  <div class="footer-brand">
    <div class="name">brindleroofing</div>
    <p>Brindle Roofing Ltd is registered in England as a private limited company.</p>
    <p style="margin-top:14px">Registration No: 04712958</p>
    <p style="margin-top:14px">Registered Office: Unit 14b Elm Yard, Mill Lane, Writtle, Chelmsford CM1 3XY</p>
  </div>
  <div class="badges">
    <div class="badge" style="width:58px;height:28px;border-radius:4px"></div>
    <div class="badge" style="width:56px;height:20px;border-radius:3px"></div>
    <div class="badge" style="width:58px;height:26px;border-radius:3px"></div>
    <div class="badge" style="width:38px;height:38px;border-radius:50%"></div>
  </div>
  <div class="footer-rule"></div>
  <div class="copyright">© Copyright Brindle Roofing Ltd 2023 | All rights reserved.</div>
</footer>

</body>
</html>
```